App UI Design: Shopping/E-commerce App

Project :
Develop an UI design & App icon for an E-commerce/Shopping App

About the App/ Target Audience:
This grocery & food shopping app will be used by independent pub, café, restaurant owners to place & manage their purchases of foods and groceries for their catering businesses.

They will use the app to access product catalogues & special promotions, search & buy large quantities of groceries or catering supplies, and the ability to manage and track status of their order.

The HTML5 App’s has been built with a very basic structure. It now needs the visual layer of the UI designed

Note:
The app is tailored for business & catering orders, not retail/supermarket buyers, so the visual needs to look smart & not too casual.

Reason: Current submissions have not met out expectations. Please use the similar app examples in the PDF as a strong point of reference for the look & feel. Feedback will be given as submissions come in, please feel free to submit initial concepts of 1 or 2 of the pages & we'll provide feedback on whether it is on the right track or not before you do more work. Current submission will also receive feedback in the next few days. We look forward to new submissions!

Target Market(s)

Male & Female. Independent pub, café, restaurant owners buying for their catering businesses. Chefs etc.

Industry/Entity Type

Restaurant

Requirements
Must have
• An overview of elements/pages of the app that needs to be designed are:
(DOWNLOAD a more detailed diagram PDF explanation)

1. Welcome- Log-in Page
2. Homepage – index that links to different function of the app

Products:
3. Promotions page – for products on special for a limited time
4. Catalogue page – access to a range of catalogue

Ways to buy:
5. Basket (Shopping Cart) - tracking items they are buying from the catalogues
6. Templates (Pre-set Shopping list)- Set shopping list that has been preloaded for certain menu
7. Open Order page

My Account:
8. My Account/profile page – Users can check the status of their order, look at past orders, look at their account number & details etc

_______________________________________________________

Icon set- Icons to represent each pages that act as visual cues for easier browsing.

2 Main features that need to be accessible & consistent throughout all pages are:
a) The Navigation Bar –
so the user can quickly find their way back & access to the main functions
b) The Search bar –
whether it drops down when needed, or is featured as a header/footer.
c) Log out button
Nice to have
• _______________________________________________________

Things to keep in mind:

The UI design essentially needs to be a customizable template that can easily adapt to any brand/logo with a slight change of the color scheme. As we will later implement our brand & logo onto it.

We’re looking for a clean & clear design that allows for a straight forward easy user experience.

You are free to develop different layout & UI pattern that you feel is the most efficient way the user can walk through the App & make their purchase in no more than 2 or 3 clicks
________________________________________________

Screenshot of Similar Apps for reference are also in the PDF

```html
<!DOCTYPE html>
<html lang="en">
<head>
<meta charset="utf-8">
<title>Catering Supplies App – Login and Home</title>
<link href="https://fonts.googleapis.com/css2?family=Comfortaa:wght@300;400&family=Open+Sans:wght@400;600;700&family=Share+Tech+Mono&display=swap" rel="stylesheet">
<style>
  :root {
    --stage-top: #ffffff;
    --stage-bottom: #6cbdc1;
    --screen-light: #e4e7ee;
    --screen-mid: #cfd4dd;
    --screen-dark: #b9bfcb;
    --field-blue: #5278c4;
    --field-edge: #ffffff;
    --field-text: #2d4a86;
    --button-dark: #173f8e;
    --button-light: #3a6fd0;
    --icon-blue: #2a5fbe;
    --icon-deep: #12398a;
    --label-grey: #4a4f58;
    --logo-grey: #8c9097;
    --header-light: #f4f4f4;
    --header-dark: #c8c8c8;
    --tab-top: #7e9fd8;
    --tab-bottom: #3a5a98;
    --tab-active: #d9dadd;
  }
  * { box-sizing: border-box; margin: 0; padding: 0; }
  html, body { width: 1200px; height: 832px; overflow: hidden; }
  body {
    position: relative;
    background: linear-gradient(180deg, var(--stage-top) 0%, var(--stage-top) 10%, #c7e6e7 45%, var(--stage-bottom) 100%);
    font-family: "Open Sans", sans-serif;
  }
  .screen {
    position: absolute;
    top: 145px;
    width: 385px;
    height: 578px;
    overflow: hidden;
    box-shadow: 0 2px 8px rgba(0,0,0,.35);
    background:
      linear-gradient(115deg, transparent 0%, rgba(255,255,255,.35) 20%, transparent 32%, rgba(255,255,255,.3) 50%, transparent 62%, rgba(255,255,255,.25) 80%, transparent 92%),
      linear-gradient(180deg, var(--screen-light), var(--screen-mid) 60%, var(--screen-dark));
  }
  .screen--login { left: 178px; }
  .screen--home { left: 610px; }

  /* Login */
  .brand-name {
    position: absolute; top: 96px; left: 0; width: 100%;
    text-align: center;
    font-family: "Comfortaa", sans-serif; font-weight: 300;
    font-size: 50px; letter-spacing: 2px;
    color: var(--logo-grey);
  }
  .field {
    position: absolute; left: 73px; width: 239px; height: 40px;
    background: var(--field-blue);
    border: 2px solid var(--field-edge);
    border-radius: 6px;
    box-shadow: inset 0 2px 4px rgba(0,0,0,.35), 0 6px 6px -3px rgba(0,0,0,.25);
    color: var(--field-text);
    font-size: 19px; padding: 6px 12px; line-height: 24px;
  }
  .field--username { top: 245px; }
  .field--password { top: 313px; }
  .forgot-link {
    position: absolute; top: 372px; left: 0; width: 100%;
    text-align: center;
    font-family: "Comfortaa", sans-serif; font-size: 16px; color: #222;
  }
  .sign-in {
    position: absolute; top: 431px; left: 115px; width: 157px; height: 50px;
    border-radius: 4px;
    border: 2px solid #0c2556;
    background: radial-gradient(ellipse at 50% 100%, #4f8ae8 0%, var(--button-light) 25%, var(--button-dark) 70%);
    box-shadow: 0 3px 4px rgba(0,0,0,.4);
    color: #fff; font-size: 21px; text-align: center; line-height: 45px;
  }

  /* Home */
  .app-header {
    position: absolute; top: 0; left: 0; width: 100%; height: 54px;
    background: linear-gradient(180deg, var(--header-light), var(--header-dark));
    border-bottom: 1px solid #9a9a9a;
    box-shadow: 0 2px 4px rgba(0,0,0,.25);
    border-radius: 4px 4px 0 0;
  }
  .search-bar {
    position: absolute; top: 13px; left: 81px; width: 223px; height: 28px;
    background: #fff; border: 2px solid #b9b9b9; border-radius: 3px;
    font-size: 13px; color: #555; padding: 4px 6px;
  }
  .search-bar svg { position: absolute; right: 5px; top: 2px; }
  .logout-button { position: absolute; top: 12px; left: 344px; }
  .feature {
    position: absolute; width: 150px; text-align: center;
  }
  .feature svg { display: block; margin: 0 auto; filter: drop-shadow(1px 3px 2px rgba(0,0,0,.35)); }
  .feature__label {
    margin-top: 2px;
    font-family: "Share Tech Mono", monospace; font-size: 15px; font-weight: 700;
    color: var(--label-grey); letter-spacing: .5px;
    text-shadow: 0 1px 0 #fff;
  }
  .col-1 { left: 42px; }
  .col-2 { left: 186px; }
  .row-1 { top: 128px; }
  .row-2 { top: 245px; }
  .row-3 { top: 360px; }

  .tab-bar {
    position: absolute; left: 0; bottom: 0; width: 100%; height: 58px;
    background: linear-gradient(180deg, var(--tab-top), var(--tab-bottom));
    border-top: 1px solid #2b4478;
    display: flex;
  }
  .tab {
    flex: 1; text-align: center; padding-top: 5px;
    color: #fff; font-size: 11px; font-weight: 700;
  }
  .tab svg { display: block; margin: 0 auto 1px; }
  .tab--active {
    flex: 0 0 120px; margin: 3px 10px 3px 6px;
    background: linear-gradient(180deg, #eceded, var(--tab-active));
    border-radius: 2px; color: #222; padding-top: 2px;
  }
</style>
</head>
<body>

<section class="screen screen--login" aria-label="Login screen">
  <div class="brand-name">LOGO</div>
  <div class="field field--username">Username</div>
  <div class="field field--password">Password</div>
  <div class="forgot-link">Forgot?</div>
  <div class="sign-in">Sign in</div>
</section>

<section class="screen screen--home" aria-label="Home screen">
  <header class="app-header">
    <div class="search-bar">Search
      <svg width="14" height="20" viewBox="0 0 14 20"><circle cx="7" cy="6" r="4.5" fill="none" stroke="#333" stroke-width="2"/><line x1="7" y1="10.5" x2="7" y2="19" stroke="#333" stroke-width="2"/></svg>
    </div>
    <svg class="logout-button" width="36" height="30" viewBox="0 0 36 30">
      <path d="M22 6 A11 11 0 1 0 22 24" fill="none" stroke="#fff" stroke-width="5" stroke-linecap="round"/>
      <path d="M12 15 H30 M24 9 L31 15 L24 21" fill="none" stroke="#fff" stroke-width="4" stroke-linecap="round" stroke-linejoin="round"/>
    </svg>
  </header>

  <div class="feature col-1 row-1">
    <svg width="74" height="74" viewBox="0 0 74 74">
      <circle cx="37" cy="37" r="34" fill="var(--icon-blue)" stroke="#0d2f73" stroke-width="3"/>
      <ellipse cx="37" cy="24" rx="24" ry="14" fill="#fff" opacity=".25"/>
      <rect x="32" y="12" width="10" height="34" rx="5" fill="#fff"/>
      <circle cx="37" cy="56" r="6" fill="#fff"/>
    </svg>
    <div class="feature__label">PROMOTIONS</div>
  </div>

  <div class="feature col-2 row-1">
    <svg width="76" height="76" viewBox="0 0 76 76">
      <path d="M10 4 H62 L72 14 V74 H10 Z" fill="var(--icon-blue)" stroke="#0d2f73" stroke-width="2"/>
      <rect x="24" y="18" width="34" height="14" fill="#fff" opacity=".9"/>
      <rect x="28" y="22" width="26" height="6" fill="var(--icon-deep)"/>
      <g fill="#fff"><rect x="4" y="24" width="10" height="4"/><rect x="4" y="36" width="10" height="4"/><rect x="4" y="48" width="10" height="4"/></g>
    </svg>
    <div class="feature__label">CATALOGUE</div>
  </div>

  <div class="feature col-1 row-2">
    <svg width="80" height="74" viewBox="0 0 80 74">
      <path d="M4 4 L14 10 L22 46 H66" fill="none" stroke="var(--icon-blue)" stroke-width="6" stroke-linejoin="round" stroke-linecap="round"/>
      <path d="M18 16 H74 L66 40 H24 Z" fill="var(--icon-blue)" stroke="#0d2f73" stroke-width="2"/>
      <g stroke="#fff" stroke-width="2" opacity=".7"><line x1="34" y1="18" x2="36" y2="38"/><line x1="46" y1="18" x2="46" y2="38"/><line x1="58" y1="18" x2="56" y2="38"/></g>
      <line x1="26" y1="60" x2="62" y2="60" stroke="var(--icon-blue)" stroke-width="4"/>
      <circle cx="26" cy="62" r="7" fill="var(--icon-blue)" stroke="#0d2f73" stroke-width="2"/>
      <circle cx="62" cy="62" r="7" fill="var(--icon-blue)" stroke="#0d2f73" stroke-width="2"/>
    </svg>
    <div class="feature__label">BASKET</div>
  </div>

  <div class="feature col-2 row-2">
    <svg width="70" height="70" viewBox="0 0 70 70">
      <rect x="3" y="3" width="64" height="64" fill="var(--icon-blue)" stroke="#0d2f73" stroke-width="2"/>
      <g fill="#fff"><rect x="10" y="8" width="4" height="4"/><rect x="18" y="8" width="4" height="4"/><rect x="26" y="8" width="4" height="4"/></g>
      <rect x="10" y="17" width="50" height="42" fill="none" stroke="#fff" stroke-width="3"/>
      <line x1="10" y1="26" x2="60" y2="26" stroke="#fff" stroke-width="3"/>
      <line x1="24" y1="26" x2="24" y2="59" stroke="#fff" stroke-width="3"/>
    </svg>
    <div class="feature__label">ORDER TEMPLATE</div>
  </div>

  <div class="feature col-1 row-3">
    <svg width="80" height="66" viewBox="0 0 80 66">
      <path d="M6 6 H44 V14 H14 V54 H44 V46 H52 V62 H6 Z" fill="var(--icon-blue)" stroke="#0d2f73" stroke-width="2"/>
      <path d="M22 50 C24 32 38 24 56 24 V14 L76 30 L56 46 V36 C40 36 30 40 22 50 Z" fill="var(--icon-blue)" stroke="#0d2f73" stroke-width="2"/>
    </svg>
    <div class="feature__label">OPEN ORDER</div>
  </div>

  <div class="feature col-2 row-3">
    <svg width="60" height="72" viewBox="0 0 60 72">
      <circle cx="30" cy="16" r="14" fill="var(--icon-blue)" stroke="#0d2f73" stroke-width="2"/>
      <path d="M4 70 V58 C4 42 16 34 30 34 C44 34 56 42 56 58 V70 Z" fill="var(--icon-blue)" stroke="#0d2f73" stroke-width="2"/>
      <ellipse cx="30" cy="44" rx="18" ry="6" fill="#fff" opacity=".25"/>
    </svg>
    <div class="feature__label">MY ACCOUNT</div>
  </div>

  <nav class="tab-bar">
    <div class="tab">
      <svg width="32" height="32" viewBox="0 0 32 32"><circle cx="16" cy="16" r="15" fill="#fff"/><path d="M10 10 L22 22 M22 10 L10 22" stroke="var(--icon-blue)" stroke-width="4" stroke-linecap="round"/></svg>
      Iconn.01
    </div>
    <div class="tab">
      <svg width="32" height="32" viewBox="0 0 32 32"><circle cx="16" cy="16" r="15" fill="#dde2ea"/><path d="M10 10 L22 22 M22 10 L10 22" stroke="#5a6f96" stroke-width="4" stroke-linecap="round"/></svg>
      Iconn.02
    </div>
    <div class="tab tab--active">
      <svg width="32" height="32" viewBox="0 0 32 32"><circle cx="16" cy="16" r="15" fill="#4a5f8c"/><path d="M10 10 L22 22 M22 10 L10 22" stroke="#c9d1e0" stroke-width="4" stroke-linecap="round"/></svg>
      Iconn.03
    </div>
  </nav>
</section>

</body>
</html>
```